Email Newsletter Header/Banner

We are an Australian Real Estate investment company that require a header for our email newsletter. Dimensions 790px by 180px.

Header must include both our website logos
http://www.kelvorplan.com.au
http://kelvorhomes.com.au

We want the header to have a human or community feel. No corporate or business look. Clean modern design
Updates

Please only use the logo of Kelvor PlanĀ http://www.kelvorplan.com.au

Target Market(s)

Real Estate Investors

Industry/Entity Type

Investment

Requirements
Must have
• Community or human feel

```html
<!DOCTYPE html>
<html lang="en">
<head>
<meta charset="utf-8">
<title>Kelvor Plan Newsletter Header</title>
<link href="https://fonts.googleapis.com/css2?family=Open+Sans:wght@400;700&display=swap" rel="stylesheet">
<style>
  :root {
    --page: #ffffff;
    --banner-bg: #ececec;
    --blue: #2f86c9;
    --grey: #9a9a9b;
    --pale-grey: #e2e2e3;
    --ink: #1d1d1f;
    --white: #ffffff;
  }
  html, body {
    margin: 0;
    padding: 0;
    width: 1200px;
    height: 278px;
    overflow: hidden;
    background: var(--page);
  }
  .canvas {
    position: relative;
    width: 1200px;
    height: 278px;
    overflow: hidden;
  }
  .banner {
    position: absolute;
    left: 76px;
    top: 54px;
    width: 1036px;
    height: 172px;
    background: var(--banner-bg);
    box-shadow: 0 2px 6px rgba(0, 0, 0, 0.35);
    overflow: hidden;
  }
  .banner-shapes {
    position: absolute;
    inset: 0;
  }
  .brand {
    position: absolute;
    left: 150px;
    top: 62px;
    display: flex;
    align-items: center;
    gap: 14px;
  }
  .brand-mark {
    width: 34px;
    height: 34px;
    background: var(--blue);
  }
  .brand-name {
    font-family: "Open Sans", Arial, sans-serif;
    font-weight: 700;
    font-size: 60px;
    line-height: 1;
    letter-spacing: -1px;
    color: var(--ink);
  }
  .tagline {
    position: absolute;
    left: 330px;
    top: 142px;
    font-family: "Open Sans", Arial, sans-serif;
    font-weight: 400;
    font-size: 11px;
    line-height: 16px;
    color: var(--white);
    white-space: nowrap;
  }
</style>
</head>
<body>
  <div class="canvas">
    <header class="banner">
      <svg class="banner-shapes" width="1036" height="172" viewBox="0 0 1036 172" aria-hidden="true">
        <polygon class="corner-pale" points="0,0 300,0 0,150" fill="var(--pale-grey)"/>
        <polygon class="corner-blue" points="0,0 158,0 0,107" fill="var(--blue)"/>
        <polygon class="corner-stripe" points="158,0 176,0 0,119 0,107" fill="var(--white)"/>
        <rect class="corner-block" x="0" y="122" width="88" height="50" fill="var(--blue)"/>
        <polygon class="side-grey" points="640,0 1036,0 1036,172 940,172 940,150" fill="var(--grey)"/>
        <polygon class="side-stripe" points="622,0 640,0 940,150 922,150" fill="var(--white)"/>
        <polygon class="tagline-bar" points="318,142 932,142 952,158 318,158" fill="var(--blue)"/>
      </svg>
      <div class="brand">
        <span class="brand-mark"></span>
        <span class="brand-name">kelvorplan.com</span>
      </div>
      <p class="tagline" style="margin:0">Newsletter for Australian Real Estate investment company- Issue no 1</p>
    </header>
  </div>
</body>
</html>
```